Kovo Pays Less! Innovative Team Buying Web App

Kovo is a team-buying/social commerce web app that is a cross between Dealvark and sites/apps like Zibo, Mervane, and Lokashwin. It is basically like a game in which users seek to get the lowest prices by working with friends and neighbours (as a team) to maximize order volumes. Sellers on the platform set volume targets which teams have to hit to secure wholesale price.
We need a landing page and a few (4 - 5) key pages that project a compelling game-like aesthetic that is innovative and playful, while being clean and classy.

Target Market(s)

Nigerian homemakers. Typically 30+ years old. Predominantly female, middle class.

Industry/Entity Type

Ecommerce, Groceries.

Coding

Coded - Design and coding required

Number of Pages Required

5+ page

Requirements
Must have
• PAGES (1). Landing page. An attractive landing page that gives a brief overview of the concept and main features. We are going to roll out an MVP with just the landing page (which should include a sign-up form) so this page is critical and should be "self-contained" with it's signup inputs. The signup section must include a referral code so that we can track who referred whom. (2). Available deals. A listing of all active deals with enough relevant information. Note that deals have a deadline, a retail price, and a minimum volume target to unlock wholesale price. (3). Deal details page. This should show the standard price (the price the user would pay if he buys a small quantity), team price (the wholesale price based on the team hitting the required order volume), the points to be earned by buying the item, etc. (4). Checkout page. In addition to normal checkout stuff on this page the user can convert points into currency (at an exchange rate that may vary from time to time). Example: if price is $3,000 he may see that he has 1000 points in his wallet and the exchange rate is 1:1, so he can go ahead and convert to $1,000 and the price now becomes $2,000. (5). Profile page. Where the user can see things like his performance (how his points were calculated), his lineage ("children" and "grandchildren"), points required to get to the next rank, his order history, etc.
Nice to have
• GUIDELINES (1). Overall Aesthetic is game-like: playful, bright, and colourful. But clean and classic at the same time: we don't want a look that goes "out of fashion" within the next two or three years. (2). Referral is critical. Therefore the "Share" button (or whatever) should be easily accessible and visible on all relevant pages. (3). The user's community is critical. Therefore the activity of the users "network" (the "children" and "grandchildren") must be somehow dynamically visible at most/all times. We want to project a sense of realtime dynamism, just like a game. The user should be able to somehow "see" things happening in the network (e.g. when someone in his network buys something). (4). Like a game, the user's points, rank, and badges must always/usually be visible and we need an interesting visual effect when something happens that increases his points. Examples of actions that generate points include buying an item, when a "child" or "grandchild" buys an item, when someone you invited/referred creates an account, etc. We need a clear idea of the visual effect and how it would work.

```html
<!DOCTYPE html>
<html lang="en">
<head>
<meta charset="utf-8">
<title>Kovo – Team Buying</title>
<link href="https://fonts.googleapis.com/css2?family=Poppins:wght@300;400;500;600;700&display=swap" rel="stylesheet">
<style>
:root{
  --backdrop:#3a3a3a;
  --page:#ffffff;
  --ink:#1f1f2b;
  --muted:#8a8d98;
  --soft:#eef0f5;
  --band:#ededed;
  --red:#ef4a3c;
  --pink:#e0457b;
  --blue:#5b6cf9;
  --link:#1a5cff;
  --line:#e6e7ec;
  --peach:#fde1cc;
}
*{box-sizing:border-box;margin:0;padding:0}
html,body{width:1200px;height:1200px;overflow:hidden;background:var(--backdrop);font-family:'Poppins',sans-serif;color:var(--ink)}
.page{position:absolute;left:412px;top:32px;width:645px;height:1830px;background:var(--page);transform:scale(0.6211);transform-origin:0 0;overflow:hidden}
.abs{position:absolute}
.logo{font-weight:700;font-size:10px;letter-spacing:.3px}
.search{left:205px;top:13px;width:222px;height:17px;border:1px solid var(--line);font-size:4px;color:var(--muted);padding:5px 6px}
.search-btn{left:414px;top:13px;width:13px;height:17px;background:#2a2316}
.auth{left:450px;top:19px;font-size:3.5px;font-weight:600}
.nav{top:46px;font-size:4.5px;font-weight:600}
.hero{left:0;top:63px;width:645px;height:242px;background:var(--soft)}
.features .item{position:absolute;top:325px;font-size:7px;font-weight:500;white-space:nowrap}
.features small{display:block;font-size:3.8px;color:var(--muted);font-weight:400}
.intro{left:55px;top:443px;width:535px;text-align:center;font-size:12.6px;line-height:18px}
.col{position:absolute;top:600px;width:160px;text-align:center;font-size:8px;line-height:13.6px;color:#444}
.col h3{font-size:10px;font-weight:400;color:var(--ink);margin-bottom:4px}
.spot{position:absolute;width:48px;height:44px;border-radius:8px}
.why{left:0;width:600px;top:714px;text-align:center;font-size:14px;font-weight:600;color:var(--blue)}
.grid{left:305px;top:808px;width:212px;height:223px;border:1px solid var(--line);display:grid;grid-template-columns:1fr 1fr}
.cell{border:1px solid #f2f2f5;padding:16px 13px}
.cell .ic{width:20px;height:20px;border-radius:50%;margin-bottom:8px;display:block}
.cell h4{font-size:7px;font-weight:600;color:var(--blue);margin-bottom:6px}
.cell p{font-size:5px;line-height:11px;color:var(--muted)}
.band{left:0;top:1088px;width:645px;height:185px;background:var(--band)}
.form{left:225px;top:1141px;width:202px;height:242px;background:#fff;box-shadow:0 2px 6px rgba(0,0,0,.12);font-size:6px}
.form label{position:absolute;left:10px;font-size:6px}
.form .in{position:absolute;left:10px;width:181px;height:17px;border:1px solid #dcdde2;font-size:6px;color:#a8aab2;padding:4px 5px}
.foot{left:0;top:1700px;width:645px;height:130px;background:var(--soft)}
.fcol{position:absolute;top:1727px;font-size:4.6px;line-height:10.8px;color:#555}
.fcol b{display:block;font-size:5px;color:var(--ink);font-weight:600;margin-bottom:4px}
</style>
</head>
<body>
<div class="page">
  <div class="abs logo" style="left:120px;top:15px">KOVO</div>
  <div class="abs search">search...</div>
  <div class="abs search-btn"><svg width="13" height="17" viewBox="0 0 13 17"><circle cx="6" cy="8" r="2.5" fill="none" stroke="#fff" stroke-width="1"/><line x1="8" y1="10" x2="9.5" y2="11.5" stroke="#fff"/></svg></div>
  <div class="abs auth">SIGN IN / SIGN UP</div>
  <svg class="abs" style="left:498px;top:15px" width="14" height="10"><rect x="1" y="2" width="7" height="7" fill="none" stroke="#222" stroke-width=".8"/><circle cx="10" cy="5" r="2" fill="var(--pink)"/></svg>
  <div class="abs nav" style="left:118px">NEW ⌄</div>
  <div class="abs nav" style="left:189px">WOMEN ⌄</div>
  <div class="abs nav" style="left:268px">MEN ⌄</div>
  <div class="abs nav" style="left:338px">KIDS ⌄</div>
  <div class="abs nav" style="left:406px">ACCESSORIES</div>
  <div class="abs nav" style="left:498px;color:var(--pink)">SALE</div>

  <div class="abs hero"></div>
  <div class="abs" style="left:93px;top:116px;font-size:4px;font-weight:600">GroupSavings</div>
  <h1 class="abs" style="left:93px;top:128px;width:240px;font-size:16.5px;line-height:24px;font-weight:700">The Ultimate Team Buying Experience</h1>
  <div class="abs" style="left:93px;top:188px;height:16px;border-left:1px solid #ccc;padding-left:5px;font-size:4.5px;color:var(--muted)">Collective Deals: Power in Numbers for Unbeatable Savings</div>
  <div class="abs" style="left:93px;top:221px;width:48px;height:18px;background:var(--red);color:#fff;font-size:5px;padding:5px 7px;white-space:nowrap">Shop Now ↗</div>
  <svg class="abs" style="left:152px;top:221px" width="20" height="20"><circle cx="10" cy="10" r="9.5" fill="#fff"/><path d="M8 7l5 3-5 3z" fill="var(--red)"/></svg>
  <div class="abs" style="left:175px;top:228px;font-size:4.5px;color:var(--muted)">What's Trending ?</div>
  <div class="abs" style="left:126px;top:284px;font-size:7px;color:var(--muted)">01 / <span style="color:var(--ink)">02</span> / 03</div>
  <div class="abs" role="img" aria-label="Photo: two happy shoppers with a phone and shopping bags" style="left:368px;top:125px;width:225px;height:180px;background:linear-gradient(160deg,#d9a98a,#6d89ad 60%,#eef0f5)"></div>

  <div class="features">
    <div class="item" style="left:93px"><svg class="abs" style="left:0;top:0" width="14" height="10"><rect x="1" y="1" width="9" height="6" fill="none" stroke="var(--red)" stroke-width=".8"/><circle cx="4" cy="8" r="1.2" fill="none" stroke="var(--red)" stroke-width=".7"/><circle cx="10" cy="8" r="1.2" fill="none" stroke="var(--red)" stroke-width=".7"/></svg><div style="margin-left:23px">Free Shipping<small>Free Shipping over $100</small></div></div>
    <div class="item" style="left:227px"><svg class="abs" width="10" height="12"><rect x="1" y="5" width="8" height="6" rx="1" fill="none" stroke="var(--red)" stroke-width=".8"/><path d="M3 5V3.5a2 2 0 014 0V5" fill="none" stroke="var(--red)" stroke-width=".8"/></svg><div style="margin-left:16px">Secure Payment<small>100% secure payment</small></div></div>
    <div class="item" style="left:349px"><svg class="abs" width="16" height="12"><circle cx="9" cy="4" r="3" fill="none" stroke="var(--red)" stroke-width=".8"/><path d="M1 10h10l3-2" fill="none" stroke="var(--red)" stroke-width=".8"/></svg><div style="margin-left:22px">Money Return<small>30 days for free return</small></div></div>
    <div class="item" style="left:474px"><svg class="abs" width="12" height="12"><path d="M2 7a4 4 0 018 0" fill="none" stroke="var(--red)" stroke-width=".8"/><rect x="1" y="7" width="2" height="3" fill="none" stroke="var(--red)" stroke-width=".7"/><rect x="9" y="7" width="2" height="3" fill="none" stroke="var(--red)" stroke-width=".7"/></svg><div style="margin-left:21px">27/7 Support<small>Support 24 hours a day</small></div></div>
  </div>

  <p class="abs intro">At Team Buying Web, we believe in the power of collaboration and the potential for extraordinary savings. We have created a platform that brings together buyers, empowering them to unlock unbeatable deals through team buying.</p>

  <div class="spot" role="img" aria-label="Illustration: market size chart" style="left:121px;top:546px;background:linear-gradient(135deg,#f3dbf5,#fbe3e8)"></div>
  <div class="col" style="left:65px"><h3>Market size</h3>400 million customers across Tier 1-4 cities and towns in India</div>
  <div class="spot" role="img" aria-label="Illustration: connected community members" style="left:294px;top:544px;background:linear-gradient(135deg,#fde3dc,#f3e0f7)"></div>
  <div class="col" style="left:238px"><h3>Social Community</h3>Is important in building trust and making people buy online together specially in high involvement and trust deficit categories</div>
  <div class="spot" role="img" aria-label="Illustration: phone with shopping categories" style="left:466px;top:546px;background:linear-gradient(135deg,#fde0e4,#ece0f8)"></div>
  <div class="col" style="left:410px"><h3>Focus Categories</h3>Have a fun and safe experience shopping online including daily essentials, home decor and apparel</div>

  <div class="abs why">Why choose us?</div>
  <svg class="abs" style="left:112px;top:757px" width="90" height="270"><path d="M0 0h43a43 43 0 0143 43v227H0V0z" fill="var(--blue)"/></svg>
  <div class="abs" role="img" aria-label="Illustration: courier delivering a parcel through a smartphone" style="left:125px;top:820px;width:110px;height:140px;background:linear-gradient(180deg,#e9d9a8,#b9aa97);border-radius:6px"></div>
  <div class="abs grid">
    <div class="cell"><svg class="ic" viewBox="0 0 20 20"><circle cx="10" cy="10" r="10" fill="var(--pink)"/><rect x="5.5" y="7" width="9" height="6" rx="1" fill="none" stroke="#fff" stroke-width="1"/><line x1="5.5" y1="9" x2="14.5" y2="9" stroke="#fff"/></svg><h4>Affordable</h4><p>Bringing our users the best prices directly from the source</p></div>
    <div class="cell"><svg class="ic" viewBox="0 0 20 20"><circle cx="10" cy="10" r="10" fill="#f6b23e"/><path d="M5 6h2l1.5 6h5l1-4H8" fill="none" stroke="#fff" stroke-width="1"/><circle cx="9" cy="14" r=".9" fill="#fff"/><circle cx="13" cy="14" r=".9" fill="#fff"/></svg><h4>Essentials</h4><p>Everyday essentials, locally manufactured products and fresh produce</p></div>
    <div class="cell"><svg class="ic" viewBox="0 0 20 20"><circle cx="10" cy="10" r="10" fill="#2aa4e8"/><rect x="5" y="8" width="10" height="4.5" rx="2.2" fill="none" stroke="#fff" stroke-width="1"/></svg><h4>Engaging</h4><p>A fun way to buy everyday essentials with your friends and family</p></div>
    <div class="cell"><svg class="ic" viewBox="0 0 20 20"><circle cx="10" cy="10" r="10" fill="#4fbf8a"/><path d="M7 6l2 2-1 1.5c.8 1.5 1.7 2.4 3 3l1.5-1 2 2-1.5 1.5C9.5 14.5 6 11 5.5 7.5z" fill="none" stroke="#fff" stroke-width=".9"/></svg><h4>Customer Service</h4><p>Providing the best support to all our customers at all times</p></div>
  </div>

  <div class="abs band"></div>
  <div class="abs" role="img" aria-label="Photo: two women in blue outfits" style="left:38px;top:1088px;width:160px;height:185px;background:linear-gradient(180deg,#ededed,#6a86c9 50%,#b3c2e6)"></div>
  <div class="abs" role="img" aria-label="Photo: woman in sunglasses, side profile" style="left:448px;top:1088px;width:152px;height:185px;background:linear-gradient(180deg,#ededed,#c69176 45%,#6f95d8)"></div>
  <div class="abs" style="left:225px;top:1108px;width:210px;text-align:center;font-size:16.5px;font-weight:700;color:#333;white-space:nowrap">Get 10% Off Signup Now</div>
  <div class="abs form">
    <div class="abs" style="right:6px;top:6px;font-size:11px;color:#777">×</div>
    <div class="abs" style="left:0;width:202px;top:26px;text-align:center;font-size:11px;font-weight:600">Sign Up</div>
    <label style="top:53px">Email</label><div class="in" style="top:64px">yourname@mail.kovo</div>
    <label style="top:91px">Phone</label><div class="in" style="top:102px">+1 ___ ___-___</div>
    <label style="top:129px">Referral Code</label><div class="in" style="top:140px"><span style="position:absolute;right:5px;top:3px;font-size:5px">◉</span></div>
    <div class="abs" style="left:10px;top:161px;font-size:3.5px;color:#aaa;white-space:nowrap">8 or more characters, at least 1 letter and 1 number</div>
    <div class="abs" style="left:10px;top:174px;font-size:3.8px;white-space:nowrap">✓ I agree with <span style="color:var(--link)">Terms&amp;Conditions</span></div>
    <div class="abs" style="left:76px;top:194px;width:49px;height:16px;border-radius:8px;background:var(--link);color:#fff;font-size:5px;font-weight:600;text-align:center;line-height:16px">SIGN UP</div>
    <div class="abs" style="left:0;width:202px;top:217px;text-align:center;font-size:4px;line-height:7px">Already have an account?<br><b style="color:var(--link);font-size:5px">LOG IN</b></div>
  </div>

  <div class="abs" style="left:0;width:612px;top:1406px;text-align:center;font-size:3.8px;color:#777">Testimonials</div>
  <div class="abs" style="left:0;width:628px;top:1415px;text-align:center;font-size:10px;font-weight:600">Our Happy Clients</div>
  <div class="abs" style="left:60px;top:1440px;width:150px;height:150px;border-radius:50%;background:radial-gradient(#fde9dc,transparent 70%)"></div>
  <div class="abs" role="img" aria-label="Client photo" style="left:79px;top:1493px;width:26px;height:26px;border-radius:50%;background:#d9a07c"></div>
  <div class="abs" role="img" aria-label="Client photo" style="left:133px;top:1488px;width:20px;height:20px;border-radius:50%;background:#c9b8ae"></div>
  <div class="abs" role="img" aria-label="Client photo" style="left:116px;top:1534px;width:28px;height:28px;border-radius:50%;background:#a89c93"></div>
  <div class="abs" role="img" aria-label="Client photo" style="left:81px;top:1553px;width:16px;height:16px;border-radius:50%;background:#9a88a3"></div>
  <div class="abs" role="img" aria-label="Client photo" style="left:106px;top:1580px;width:16px;height:16px;border-radius:50%;background:#6f7a86"></div>
  <div class="abs" role="img" aria-label="Client photo" style="left:145px;top:1584px;width:22px;height:22px;border-radius:50%;background:#d6c4ae"></div>
  <div class="abs" style="left:292px;top:1448px;font-size:60px;font-weight:700;color:#f1f1f3;line-height:1">”</div>
  <p class="abs" style="left:170px;top:1513px;width:163px;text-align:right;font-size:6.5px;line-height:11px;color:#888">Lorem ipsum dolor sit amet, consetetur sadipscing elitr, sed diam nonumy eirmod tempor invidunt ut labore et dolore magna.</p>
  <div class="abs" style="left:230px;width:103px;top:1552px;text-align:right;font-size:7.5px">Tobi Adeyemi</div>
  <div class="abs" style="left:230px;width:105px;top:1564px;text-align:right;font-size:5px;color:var(--red);letter-spacing:-.5px">★★★★★</div>
  <svg class="abs" style="left:289px;top:1586px" width="50" height="20"><circle cx="9" cy="10" r="9" fill="#f0f0f0"/><path d="M10 7l-3 3 3 3" fill="none" stroke="#bbb"/><circle cx="36" cy="10" r="9" fill="var(--red)"/><path d="M35 7l3 3-3 3" fill="none" stroke="#fff"/></svg>
  <div class="abs" style="left:375px;top:1473px;width:155px;height:145px;border-radius:14px;background:var(--peach)"></div>
  <div class="abs" role="img" aria-label="Photo: smiling client in a blue shirt, arms crossed" style="left:388px;top:1438px;width:130px;height:180px;background:linear-gradient(180deg,#b08a76,#7eb5d6 45%,#5f98c0)"></div>

  <div class="abs foot"></div>
  <div class="abs logo" style="left:93px;top:1726px">KOVO</div>
  <p class="abs" style="left:93px;top:1746px;width:125px;font-size:4.6px;line-height:8px;color:#555">Lorem ipsum dolor sit amet, consetetur sadipscing elitr, sed diam nonumy eirmod tempor invidunt ut labore voluptua. At vero eos.</p>
  <svg class="abs" style="left:93px;top:1788px" width="40" height="6"><circle cx="2" cy="3" r="2" fill="#333"/><circle cx="18" cy="3" r="2" fill="#333"/><circle cx="34" cy="3" r="2" fill="#333"/></svg>
  <div class="fcol" style="left:263px"><b>Information Company</b>About Us<br>Our Impact<br>Digital Payments<br>Membership<br>Terms &amp; Conditions</div>
  <div class="fcol" style="left:385px"><b>Account</b>FAQ<br>Track Your Order<br>Returns &amp; Refunds<br>Take Our Feedback<br>Contact us</div>
  <div class="fcol" style="left:505px"><b>Info</b>Terms &amp; Conditions<br>Privacy Policy<br>SitemapPrivacy<br>PolicySitemap</div>
</div>
</body>
</html>
```